Flyer-Design für Beratung, Coaching
Zielgruppe
Beratung, Coaching, Mediation. Meine Zielgruppe sind insbesondere hochgestellte Führungskräfte /Bereichsleiter, Vorstände, Geschäftsführer und Projektleiter.
Aufgabenstellung
Ich habe das neue Logo (quervoran.kollegen), den ersten Flyer, ein neues Bild und den aktuellen Text des Flyers beigefügt. beigefügt. Ich müsste im fertigen Flyer aber den Text editieren können, da ich gelegentlich neue Passagen einfügen möchte. Der Flyer sollte DIN A4 quer im Format sein, damit ich ihn falten kann. Sofern aber jemand eine andere Idee hat, nur zu. Farblich sollte natürlich das neue Logo die Gestaltung des Flyers beeinflussen. Der Flyer soll als eher exklusives Giving verwendet werden; nicht als 'Massenware'. Ich möchte den Flyer als persönliches Profildokument an ausgewählte Personen weitergeben, die mich bereits aus der Mund-zu-Mund Propaganda kennen.

```html
<!DOCTYPE html>
<html lang="de">
<head>
<meta charset="utf-8">
<title>quervoran.kollegen – Profilflyer</title>
<link href="https://fonts.googleapis.com/css2?family=Quicksand:wght@500;600&family=Varela+Round&family=Poppins:wght@400;500;600;700&family=Roboto+Condensed:wght@700&display=swap" rel="stylesheet">
<style>
:root{
  --gold:#b08e45;
  --gold-light:#c7a968;
  --teal:#2f7f8e;
  --teal-dark:#2b6d72;
  --ink:#3a3a3a;
  --paper:#ffffff;
  --backdrop:#dfe2e4;
  --navy:#2b4f8f;
  --sky:#2a96c8;
  --grey-badge:#c9c9c9;
}
*{box-sizing:border-box;margin:0;padding:0}
html,body{width:1200px;height:900px;overflow:hidden;background:var(--backdrop)}
body{position:relative;font-family:"Poppins",sans-serif;color:var(--ink)}
.sheet{position:absolute;display:flex;box-shadow:0 4px 12px rgba(0,0,0,.18)}
.sheet--cover{left:140px;top:15px}
.sheet--outer{left:467px;top:15px}
.sheet--back{left:140px;top:465px}
.sheet--inner{left:467px;top:465px}
.page{position:relative;width:297px;height:420px;background:var(--paper);overflow:hidden}
.page--soft{background:linear-gradient(180deg,#f7f8f8,#e9ecec)}
.corner{position:absolute;top:0}
.corner--left{left:0}
.corner--right{right:0}

/* cover */
.brand{position:absolute;top:135px;left:0;right:0;text-align:center;font-family:"Quicksand",sans-serif;font-weight:600;font-size:27px;color:var(--gold);letter-spacing:.2px}
.tagline{position:absolute;top:176px;left:0;right:0;text-align:center;font-size:7.5px;letter-spacing:3.4px;color:var(--gold)}
.portrait{position:absolute;top:196px;left:101px;width:94px;height:94px}
.portrait .ring{position:absolute;inset:0;border-radius:50%;background:conic-gradient(var(--gold) 0 45%,var(--teal) 45% 100%)}
.portrait .photo{position:absolute;top:4px;left:6px;width:84px;height:84px;border-radius:50%;background:radial-gradient(circle at 50% 40%,#b9a594,#5e5149 70%,#2f2a27)}
.band{position:absolute;left:0;right:0}
.band .stripe{height:10px;background:var(--teal-dark)}
.band .bar{height:20px;background:var(--gold);color:#fff;text-align:center;font-family:"Varela Round",sans-serif;font-size:11.5px;letter-spacing:1.4px;line-height:20px}
.band--cert{top:286px}
.award-title{position:absolute;top:321px;left:0;right:0;text-align:center;font-weight:700;font-size:11px;letter-spacing:2px;color:var(--gold)}
.award-list{position:absolute;top:337px;left:0;right:0;text-align:center;font-size:6.4px;line-height:9px;color:#333}
.badges{position:absolute;top:360px;left:12px;right:12px;height:52px}
.badge{position:absolute}
.badge--round{left:0;top:0;width:50px;height:50px;border-radius:50%;background:var(--navy);border:3px solid #fff;box-shadow:0 0 0 1.5px var(--navy)}
.badge--block{left:100px;top:6px;width:72px;height:40px;background:var(--grey-badge);opacity:.7}
.badge--disc{right:0;top:2px;width:48px;height:48px;border-radius:50%;background:var(--sky)}

/* qualification */
.qual-heading{position:absolute;top:4px;left:140px;font-family:"Varela Round",sans-serif;font-size:26px;line-height:30px;color:var(--teal-dark);transform:rotate(42deg);transform-origin:left center;letter-spacing:1px;-webkit-text-stroke:.7px var(--teal-dark);white-space:nowrap}
.qual-list{position:absolute;top:70px;left:22px;width:240px;font-family:"Varela Round",sans-serif;font-size:9px;line-height:12px;color:#333;letter-spacing:.4px}
.qual-item{margin-bottom:12px}
.qual-item--narrow{max-width:160px}
.qual-item .title{color:var(--gold)}
.qual-item .title span{color:#333}
.band--contact{top:286px}
.contact{position:absolute;top:322px;left:0;right:0;text-align:center;font-family:"Varela Round",sans-serif}
.contact .name{font-family:"Poppins",sans-serif;font-weight:700;font-size:12px;color:#333}
.contact .addr{font-family:"Poppins",sans-serif;font-size:12px;line-height:15px;color:#333}
.contact .reach{font-size:10px;line-height:13.5px;color:var(--gold);margin-top:3px}

/* inside spread */
.inner-left{background:#f4f6f6}
.inner-right{background:#eef1f2}
.section-title{position:absolute;left:0;right:0;text-align:center}
.services-title{top:17px;font-family:"Varela Round",sans-serif;font-size:17px;letter-spacing:2px;color:var(--teal-dark);-webkit-text-stroke:.5px var(--teal-dark)}
.services-sub{position:absolute;top:40px;left:0;right:0;text-align:center;font-size:6.2px;color:var(--gold);font-weight:500}
.services{position:absolute;top:48px;left:16px;right:16px;text-align:center;font-size:5.2px;line-height:6.8px;color:#3a3a3a}
.services .sep{color:var(--teal);font-size:7px;line-height:9px;display:block}
.services .sub{color:var(--gold);font-weight:700;font-size:7px;line-height:9px;display:block;margin-top:3px}
.services .hl{color:var(--teal);font-weight:600}
.services p{margin-bottom:2px}
.services .tight{font-size:4.6px;line-height:5.9px}
.fields-title{top:22px;font-family:"Roboto Condensed",sans-serif;font-size:21px;color:var(--gold);letter-spacing:.5px}
.fields{position:absolute;top:58px;left:14px;right:14px;text-align:center}
.field{margin-bottom:11px;font-size:6px;line-height:7.5px;color:#333}
.field .head{display:block;font-family:"Varela Round",sans-serif;font-size:8.4px;line-height:10px;color:var(--teal-dark);letter-spacing:.3px;-webkit-text-stroke:.25px var(--teal-dark)}
.field .head span{color:#333;-webkit-text-stroke:.25px #333}
.field em{font-weight:600}
.closing{position:absolute;top:350px;left:0;right:0;text-align:center;font-family:"Varela Round",sans-serif;font-size:11.5px;line-height:15px;color:var(--gold);-webkit-text-stroke:.35px var(--gold)}
.closing .teal{color:var(--teal-dark);-webkit-text-stroke:.35px var(--teal-dark)}
.deco{position:absolute;inset:0;pointer-events:none}
</style>
</head>
<body>

<div class="sheet sheet--cover">
  <section class="page cover">
    <svg class="corner corner--left" width="130" height="140" viewBox="0 0 130 140"><polygon points="0,0 102,0 0,118" fill="var(--gold)"/><polygon points="102,0 120,0 0,138 0,118" fill="var(--teal)"/></svg>
    <div class="brand">quervoran.kollegen</div>
    <div class="tagline">BERATUNG I COACHING I MEDIATION</div>
    <div class="portrait"><div class="ring"></div><div class="photo" role="img" aria-label="Porträtfoto des Beraters"></div></div>
    <div class="band band--cert"><div class="stripe"></div><div class="bar">Zertifizierungen &amp; Auszeichnungen</div></div>
    <div class="award-title">PREISTRÄGER</div>
    <div class="award-list">- deutscher Weiterbildungspreis 2004<br>- deutscher HR-Praxis- preis 2007</div>
    <div class="badges"><div class="badge badge--round"></div><div class="badge badge--block"></div><div class="badge badge--disc"></div></div>
  </section>
</div>

<div class="sheet sheet--outer">
  <section class="page page--soft qualification">
    <svg class="corner corner--right" width="180" height="150" viewBox="0 0 180 150"><polygon points="60,0 180,0 180,140" fill="var(--gold)"/><polygon points="78,0 180,0 180,118" fill="var(--teal)"/></svg>
    <div class="qual-heading">Qualifikation</div>
    <div class="qual-list">
      <div class="qual-item qual-item--narrow"><div class="title">Dipl. Betriebswirt</div>Mainufer Hochschule für Finanzen und Management – 4 Jahre</div>
      <div class="qual-item"><div class="title">Bankkaufmann IHK</div></div>
      <div class="qual-item"><div class="title">Coach (BCV)</div>2 Jahre kbo – Kreis für Beratungs- und Organisationsentwicklung</div>
      <div class="qual-item"><div class="title">Wirtschaftsmediator <span>(2 Jahre)</span></div>Hochschule Nordküste</div>
      <div class="qual-item"><div class="title">General Management Programm</div>Verbundbank Gruppe, 2 Jahre Berliner Managementschule</div>
    </div>
    <div class="band band--contact"><div class="stripe"></div><div class="bar">KONTAKT</div></div>
    <div class="contact">
      <div class="name">Matthias Kernen</div>
      <div class="addr">Lindenallee 7<br>61118 Waldheim</div>
      <div class="reach">Phone: +49 170 4418207<br>Mail: mkernen@quervoran.kollegen<br>Web: www://quervoran.kollegen</div>
    </div>
  </section>
  <section class="page page--soft cover">
    <svg class="corner corner--left" width="130" height="140" viewBox="0 0 130 140"><polygon points="0,0 102,0 0,118" fill="var(--gold)"/><polygon points="102,0 120,0 0,138 0,118" fill="var(--teal)"/></svg>
    <div class="brand">quervoran.kollegen</div>
    <div class="tagline">BERATUNG I COACHING I MEDIATION</div>
    <div class="portrait"><div class="ring"></div><div class="photo" role="img" aria-label="Porträtfoto des Beraters"></div></div>
    <div class="band band--cert"><div class="stripe"></div><div class="bar">Zertifizierungen &amp; Auszeichnungen</div></div>
    <div class="award-title">PREISTRÄGER</div>
    <div class="award-list">- deutscher Weiterbildungspreis 2004<br>- deutscher HR-Praxis- preis 2007</div>
    <div class="badges"><div class="badge badge--round"></div><div class="badge badge--block"></div><div class="badge badge--disc"></div></div>
  </section>
</div>

<div class="sheet sheet--back">
  <section class="page qualification">
    <svg class="corner corner--right" width="180" height="150" viewBox="0 0 180 150"><polygon points="60,0 180,0 180,140" fill="var(--gold)"/><polygon points="78,0 180,0 180,118" fill="var(--teal)"/></svg>
    <div class="qual-heading">Qualifikation</div>
    <div class="qual-list">
      <div class="qual-item qual-item--narrow"><div class="title">Dipl. Betriebswirt</div>Mainufer Hochschule für Finanzen und Management – 4 Jahre</div>
      <div class="qual-item"><div class="title">Bankkaufmann IHK</div></div>
      <div class="qual-item"><div class="title">Coach (BCV)</div>2 Jahre kbo – Kreis für Beratungs- und Organisationsentwicklung</div>
      <div class="qual-item"><div class="title">Wirtschaftsmediator <span>(2 Jahre)</span></div>Hochschule Nordküste</div>
      <div class="qual-item"><div class="title">General Management Programm</div>Verbundbank Gruppe, 2 Jahre Berliner Managementschule</div>
    </div>
    <div class="band band--contact"><div class="stripe"></div><div class="bar">KONTAKT</div></div>
    <div class="contact">
      <div class="name">Matthias Kernen</div>
      <div class="addr">Lindenallee 7<br>61118 Waldheim</div>
      <div class="reach">Phone: +49 170 4418207<br>Mail: mkernen@quervoran.kollegen<br>Web: www://quervoran.kollegen</div>
    </div>
  </section>
</div>

<div class="sheet sheet--inner">
  <section class="page inner-left services-page">
    <svg class="deco" width="297" height="420" viewBox="0 0 297 420">
      <polygon points="0,0 50,0 26,22" fill="var(--gold-light)"/>
      <polygon points="0,18 28,38 0,62" fill="var(--teal)" opacity=".8"/>
      <polygon points="297,0 297,4 250,20 262,0" fill="var(--gold-light)"/>
      <polygon points="297,0 297,58 262,30" fill="var(--teal)" opacity=".85"/>
      <polygon points="0,360 0,420 40,420" fill="var(--gold)"/>
      <polygon points="297,355 297,420 255,420" fill="var(--teal-dark)"/>
    </svg>
    <div class="section-title services-title">UNSERE LEISTUNGEN</div>
    <div class="services-sub">Ich unterstütze Führungspersonen in Spitzenpositionen bei:</div>
    <div class="services">
      <span class="sep">✳</span>
      <p>Erfolgreicher Bewältigung anspruchsvoller Managementphasen.</p>
      <span class="sep">✳</span>
      <p>Übernahme einer neuen Position,<br>herausfordernden strategischen Implementierungen, Turnaround-Situationen.</p>
      <span class="sep">✳</span>
      <p>Moderation von Konflikten zwischen<br>Eigentümer, Aufsichtsgremium und oberster Führungsebene.</p>
      <span class="sep">✳</span>
      <p>Begleitung in Konflikten im obersten Führungsteam,<br>bei sensiblen personellen Einzelsituationen auf den Topebenen<br>und<br>bei der Umsetzung personalpolitisch herausfordernder Maßnahmen.</p>
      <span class="sep">✳</span>
      <span class="sub" style="margin-top:0">Zielgruppen:</span>
      <p>Top-Führungspersonen, Vorstände und Aufsichtsräte.</p>
      <span class="sub">Tätigkeitsbereiche:</span>
      <p>Coaching, Executive Advisory, Restrukturierungen und Change Management.</p>
      <span class="sep">✳</span>
      <span class="sub" style="margin-top:0">Position Counseling</span>
      <p class="tight"><span class="hl">Individuelle Einzelberatung</span>, die sich ganz mit der Person und dem Kontext der aktuellen Herausforderungen befasst.<br>360°-Check auf alle vernetzten (Teil-)Aspekte von Managementthemen, Transformations-Prozessen und mikropolitischen Verhältnissen.<br><b>Trittsicherheit</b> und die <b>Festigung</b> der aktuellen Position stehen hierbei im Mittelpunkt meiner Unterstützungsleistungen.</p>
      <span class="sub">Coaching</span>
      <p class="tight"><span class="hl">Professionelle Beratung, Begleitung</span> und <span class="hl">Unterstützung</span><br>zur Steigerung und dem Erhalt der Leistungsfähigkeit.<br>Im Coaching unterstütze ich die <i>persönliche</i> und <i>berufliche Weiterentwicklung</i>, die <b>Selbstorganisation</b> und das <b>Selbstverständnis</b>.<br>Der Klient erhält die Möglichkeit, über sich selbst nachzudenken, neue Fähigkeiten zu erlernen und neue Perspektiven einzunehmen.</p>
      <span class="sub">Mediation</span>
      <p class="tight"><span class="hl">Unterstützung bei Konfliktlösungen</span>,<br>die für alle Beteiligten <b>gewinnbringend</b> und daher <b>nachhaltig</b> sind.<br><span class="hl">Professionelle Begleitung</span> unter anderem bei allen kritischen Themen der Mitarbeiterführung bis hin zu Ausscheidensvereinbarungen und Kündigungen, bei Differenzen im Zusammenhang mit Umstrukturierungen, Fusionen, Unternehmensnachfolgen, bei Verhandlungen mit den Personalvertretungen und Unstimmigkeiten innerhalb einer oder zwischen mehreren Organisationseinheiten und vielem mehr.</p>
    </div>
  </section>
  <section class="page inner-right fields-page">
    <svg class="deco" width="297" height="420" viewBox="0 0 297 420">
      <polygon points="0,18 38,36 0,58" fill="var(--gold)"/>
      <polygon points="0,26 22,36 0,48" fill="var(--teal-dark)"/>
      <polygon points="297,18 297,64 258,40" fill="var(--gold)"/>
      <polygon points="297,28 297,64 268,42" fill="var(--teal-dark)"/>
      <polygon points="0,0 0,8 14,0" fill="var(--teal)"/>
      <polygon points="297,360 297,420 265,420" fill="var(--gold)"/>
    </svg>
    <div class="section-title fields-title">ERFAHRUNGSFELDER</div>
    <div class="fields">
      <div class="field"><span class="head" style="letter-spacing:1.2px">AUFSICHTSRATSMANDATE</span>in der <em><i>Beratungsbranche</i></em> für interaktive Lernmedien seit 2001<br>und<br>im <em><i>betrieblichen Gesundheitsmanagement</i></em> seit 2012</div>
      <div class="field"><span class="head">Sparingspartner <span>und</span> Berater</span>für Vorstand und Aufsichtsrat</div>
      <div class="field"><span class="head">Verantwortung</span>für unternehmensweite <em>Restrukturierungen</em> und <em>Personalabbau</em></div>
      <div class="field"><span class="head">Leitung</span>von <em>Kostensenkungs-</em> und <em>Effizienssteigerungsprojekten</em></div>
      <div class="field"><span class="head">Krisenmanagement, Krisenkommunikation</span></div>
      <div class="field"><span class="head">Leitung</span>von mehrjährigen <em>Changemanagementprojekten</em></div>
      <div class="field"><span class="head">Aufbau <span>und</span> Neuausrichtung</span>von <em>Organisationseinheiten</em></div>
      <div class="field"><span class="head">Führung</span>von Einheiten mit über <em>200</em> Mitarbeitern</div>
    </div>
    <div class="closing">Seit über 20 Jahren<br><span class="teal">in großen</span> Inhouse-Projekten<br>und<br><span class="teal">als externer</span> Berater <span class="teal">und</span> Coach <span class="teal">tätig.</span></div>
  </section>
</div>

</body>
</html>
```